Entertainment Sound and Lighting company Business card

We need a professional looking business card designed for my growing entertainment sound and lighting company based in Sydney, Australia called "Kestrel Sound"

We provide technical production services (sound systems/lighting/vision) for events ranging from band gigs, weddings, corporate functions etc.

The business card needs to contain the following information:

Bartholomew Quenneville
Audio Engineer
Phone: 0478 615 702
Email: bartholomew@kestrelsound.com.au
Website: www.kestrelsound.com.au

Business logo has been attached in .ai format, please contact me if you need me to provide other files.

Target Market(s)

We need a business card that reflects our modern and professional company but still looks professional to appeal to our corporate clients.
We have a very broad target market spanning from bands needing PA systems for their gigs (18-30yrs) to event companies needing sound and lighting for weddings and other functions.

Industry/Entity Type

Business

Requirements
Must have
• Needs to include the logo that is attached of course, and the colour scheme.
Nice to have
• - Double sided

```html
<!DOCTYPE html>
<html lang="en">
<head>
<meta charset="utf-8">
<title>Kestrel Sound – Business Card</title>
<link rel="stylesheet" href="https://fonts.googleapis.com/css2?family=Alegreya+Sans:wght@400;500;700;800&display=swap">
<style>
  :root {
    --page-bg: #ffffff;
    --card-border: #a9bccb;
    --brand-blue: #1b8fd2;
    --back-top: #5ccdf0;
    --back-bottom: #17b6e3;
    --text-light: #ffffff;
    --text-soft: #e6f7fd;
    --link-dark: #0d5a98;
  }
  * { box-sizing: border-box; margin: 0; padding: 0; }
  html, body {
    width: 1200px;
    height: 900px;
    overflow: hidden;
    background: var(--page-bg);
    font-family: "Alegreya Sans", sans-serif;
  }
  .card {
    position: absolute;
    left: 274px;
    width: 652px;
    height: 372px;
  }
  .card-front {
    top: 38px;
    background: var(--page-bg);
    border: 2px solid var(--card-border);
    display: flex;
    align-items: center;
    justify-content: center;
  }
  .brand-name {
    font-weight: 800;
    font-size: 72px;
    letter-spacing: -1px;
    color: var(--brand-blue);
    line-height: 1;
  }
  .card-back {
    top: 484px;
    background: linear-gradient(180deg, var(--back-top) 0%, var(--back-bottom) 100%);
  }
  .contact {
    position: absolute;
    left: 296px;
    top: 150px;
    color: var(--text-light);
  }
  .contact-name {
    font-size: 25px;
    font-weight: 400;
    line-height: 1.1;
  }
  .contact-role {
    font-size: 19px;
    color: var(--text-soft);
    line-height: 1.2;
    margin-bottom: 24px;
  }
  .contact-phone {
    font-size: 21px;
    line-height: 1.3;
  }
  .contact-email {
    font-size: 19px;
    color: var(--text-soft);
    line-height: 1.4;
    margin-bottom: 16px;
  }
  .contact-web {
    font-size: 21px;
    font-weight: 700;
    color: var(--link-dark);
  }
</style>
</head>
<body>
  <section class="card card-front">
    <div class="brand-name">Kestrel Sound</div>
  </section>

  <section class="card card-back">
    <div class="contact">
      <p class="contact-name">Bartholomew Quenneville</p>
      <p class="contact-role">Audio Engineer</p>
      <p class="contact-phone">Phone: 0478 615 702</p>
      <p class="contact-email">Email: bartholomew@kestrelsound.com.au</p>
      <p class="contact-web">Website: www.kestrelsound.com.au</p>
    </div>
  </section>
</body>
</html>
```